Carpet cleaning company focused on high quality needs business cards

We are a growing company that just merged with another company and need to design a new business card. We do both residential as well as commercial cleaning. We do carpet, tile & grout, upholstery, hard floors, and stain & pet odor removal. We treat our customers like family and strive to achieve outstanding results with every job.

```html
<!DOCTYPE html>
<html lang="en">
<head>
<meta charset="utf-8">
<title>Maple Steam Cleaning – Business Cards</title>
<link rel="stylesheet" href="https://fonts.googleapis.com/css2?family=Open+Sans:wght@400;600;700;800&display=swap">
<style>
  :root {
    --bg: #2e2e2f;
    --card: #ffffff;
    --card-shade: #f1f1f1;
    --red: #e63b36;
    --blue: #1f7fc1;
    --ink: #2b2b2b;
    --muted: #444444;
  }
  * { box-sizing: border-box; margin: 0; padding: 0; }
  html, body { width: 1200px; height: 900px; overflow: hidden; }
  body {
    background: var(--bg);
    font-family: "Open Sans", Arial, sans-serif;
    color: var(--ink);
    position: relative;
  }
  .card {
    position: absolute;
    width: 620px;
    height: 354px;
    background: linear-gradient(135deg, var(--card-shade) 0%, var(--card) 55%, var(--card-shade) 100%);
    overflow: hidden;
  }
  .card--back { left: 60px; top: 70px; }
  .card--front { left: 520px; top: 476px; }

  .brand {
    position: absolute;
    display: flex;
    align-items: center;
    gap: 14px;
  }
  .brand__mark {
    width: 78px; height: 78px;
    background: var(--red);
  }
  .brand__name {
    font-weight: 800;
    font-size: 22px;
    line-height: 1.05;
    color: var(--ink);
    text-transform: uppercase;
  }
  .card--back .brand { right: 60px; top: 34px; }
  .card--front .brand { right: 48px; top: 30px; }

  .section-title {
    color: var(--red);
    font-weight: 600;
    font-size: 15px;
    text-transform: uppercase;
    margin-bottom: 6px;
  }
  .list { list-style: none; font-size: 12.5px; line-height: 1.55; color: var(--muted); }

  .hours { position: absolute; left: 34px; top: 44px; }
  .services { position: absolute; left: 34px; top: 216px; }

  .tagline {
    position: absolute;
    right: 0; top: 236px;
    background: var(--red);
    color: #fff;
    font-weight: 700;
    font-size: 14px;
    padding: 8px 26px 8px 24px;
  }

  .front-deco {
    position: absolute;
    right: 0; bottom: 0;
    width: 190px; height: 170px;
    background: rgba(230, 59, 54, 0.08);
  }
  .person {
    position: absolute;
    left: 40px; right: 40px; top: 138px;
  }
  .person__head {
    display: flex;
    align-items: flex-end;
    gap: 14px;
  }
  .person__name {
    flex: none;
    color: var(--blue);
    font-weight: 600;
    font-size: 16px;
    line-height: 22px;
    text-transform: uppercase;
  }
  .person__rule {
    flex: 1;
    height: 1px;
    background: var(--red);
    margin-bottom: 1px;
  }
  .person__role { color: var(--red); font-size: 14px; margin-top: 2px; }

  .contact { position: absolute; left: 40px; top: 208px; list-style: none; }
  .contact__item {
    display: flex; align-items: flex-start; gap: 10px;
    font-size: 13px; line-height: 1.45; color: var(--muted);
    margin-bottom: 5px;
  }
  .contact__icon { width: 14px; height: 14px; flex: none; margin-top: 3px; fill: var(--red); }
</style>
</head>
<body>

<section class="card card--back">
  <div class="brand">
    <div class="brand__mark"></div>
    <div class="brand__name">Maple<br>Steam<br>Cleaning</div>
  </div>

  <div class="hours">
    <h2 class="section-title">Our Services Time</h2>
    <ul class="list">
      <li>Monday:- 9:00am - 6:00pm</li>
      <li>Tuesday:- 9:00am - 6:00pm</li>
      <li>Wednesday:- 9:00am - 6:00pm</li>
      <li>Thursday:- 9:00am - 6:00pm</li>
      <li>Friday:- 9:00am - 6:00pm</li>
      <li>Saturday-Sunday:- Closed</li>
    </ul>
  </div>

  <div class="services">
    <h2 class="section-title">Our Services</h2>
    <ul class="list">
      <li>Natural Carpets / Residential Carpet Cleaning</li>
      <li>Tile &amp; Grout / Upholstery / Hard Floors</li>
      <li>Dining Room And Office Chairs</li>
      <li>Stain &amp; Pet Odor Removal</li>
    </ul>
  </div>

  <div class="tagline">A Clean Like You've Never Seen</div>
</section>

<section class="card card--front">
  <div class="front-deco"></div>
  <div class="brand">
    <div class="brand__mark"></div>
    <div class="brand__name">Maple<br>Steam<br>Cleaning</div>
  </div>

  <div class="person">
    <div class="person__head">
      <div class="person__name">Maple Steam Care</div>
      <div class="person__rule"></div>
    </div>
    <div class="person__role">Owner</div>
  </div>

  <ul class="contact">
    <li class="contact__item">
      <svg class="contact__icon" viewBox="0 0 24 24"><path d="M6.6 10.8a15.1 15.1 0 0 0 6.6 6.6l2.2-2.2a1 1 0 0 1 1-.25 11.4 11.4 0 0 0 3.6.57 1 1 0 0 1 1 1V20a1 1 0 0 1-1 1A17 17 0 0 1 3 4a1 1 0 0 1 1-1h3.5a1 1 0 0 1 1 1c0 1.25.2 2.45.57 3.57a1 1 0 0 1-.25 1z"/></svg>
      <span>(555) 014-2087</span>
    </li>
    <li class="contact__item">
      <svg class="contact__icon" viewBox="0 0 24 24"><path d="M2 5h20v14H2z M2 5l10 8 10-8" fill="none" stroke="#e63b36" stroke-width="2"/></svg>
      <span>hello@maplesteamclean.com</span>
    </li>
    <li class="contact__item">
      <svg class="contact__icon" viewBox="0 0 24 24"><g fill="none" stroke="#e63b36" stroke-width="2"><circle cx="12" cy="12" r="9"/><path d="M3 12h18M12 3c3 3 3 15 0 18M12 3c-3 3-3 15 0 18"/></g></svg>
      <span>www.maplesteamclean.com</span>
    </li>
    <li class="contact__item">
      <svg class="contact__icon" viewBox="0 0 24 24"><path d="M12 2a7 7 0 0 0-7 7c0 5 7 13 7 13s7-8 7-13a7 7 0 0 0-7-7zm0 9.5A2.5 2.5 0 1 1 12 6.5a2.5 2.5 0 0 1 0 5z"/></svg>
      <span>Eastfield, OH, US · Brookvale, OH, US · Linden Park, OH, US · Riverton, OH, US<br>Oakridge, OH, US</span>
    </li>
  </ul>
</section>

</body>
</html>
```